Website to help people naturally reverse diabetes

Wordpress designed with elementor. it is less than 5 pages.
we help people naturally reverse their disease diabetes.
this is my domain www.bluemeadowpath.care

(my original website was www.kestrelhollow.care
but we are creating different website for different disease condition starting with diabetes.)

1. home page and with a scheduling option
2. blog page
3. Coach page
4. Contact us

Target Market(s)

1.mid age to older people mostly that are diabetic and it is mostly the American citizens but will be used internationally

Industry/Entity Type

Health care

Coding

Number of Pages Required

4 page

Colors
0054AA
0677BA
7BADD7
CADEEF
E8F1F8
00AB8E
00BBA5
67D7C9
C6EFE9
E9F9F6
A7469A
B969AE
D3A5CF
EDDBEB
F8F0F9
6B429C
8869AF
B7A5CE
E3DAEB
F3F0F8

Requirements
Must have
• clean and good fee.l lumen arc concept a. make the customer the hero. the header page picture should reveal what the customer will feel after the program. Treating the symptom I attached a picture in the file a screen shot.. Normally people treat the symptoms and not the cause. that is 1. closing the tap. 2. remove the block. 3 and them clean he spill over. but do not want to have the picture of medical doctor or nurse. I do not want to offend them we can use the same picture but without them but some way we want to communicate the message.
Nice to have
• more visual feel

```html
<!DOCTYPE html>
<html lang="en">
<head>
<meta charset="utf-8">
<title>Kestrel Hollow – Reverse Diabetes Naturally</title>
<link href="https://fonts.googleapis.com/css2?family=Pathway+Gothic+One&family=Oswald:wght@300;400;500&family=Montserrat:wght@400;500;600;700&family=Nunito:wght@400;600;700;800&family=Tinos&display=swap" rel="stylesheet">
<style>
:root{
  --blue-dark:#0054AA;--blue:#0677BA;--blue-soft:#7BADD7;
  --teal:#00AB8E;--teal-mid:#00BBA5;--teal-light:#67D7C9;--teal-pale:#C6EFE9;--teal-wash:#BFE7E1;
  --magenta:#A7469A;--magenta-mid:#B969AE;--magenta-soft:#D3A5CF;
  --purple:#6B429C;--purple-mid:#8869AF;--purple-soft:#B7A5CE;--purple-pale:#E3DAEB;
  --ink:#1b1b1b;--grey:#8a8a8a;--line:#e3e3ea;--white:#fff;
  --condensed:'Pathway Gothic One',sans-serif;
}
*{margin:0;padding:0;box-sizing:border-box}
html,body{width:1200px;height:5372px;overflow:hidden}
body{position:relative;background:var(--white);font-family:'Montserrat',sans-serif;color:var(--ink)}
.abs{position:absolute}

/* hero */
.hero{left:0;top:0;width:1200px;height:760px;background:linear-gradient(180deg,#5d6f78 0%,#42564f 30%,#2f3e34 55%,#4f5a5c 70%,#3b3128 100%)}
.nav{left:48px;top:38px;width:1152px;height:100px;background:var(--white);border-radius:20px 0 0 20px}
.brand{left:74px;top:38px;display:flex;align-items:center;gap:10px;font-family:'Montserrat',sans-serif;font-weight:700;font-size:17px;color:var(--blue-dark)}
.brand-dot{width:20px;height:20px;border-radius:50%;background:var(--teal)}
.nav-link{top:32px;font-family:'Tinos',serif;font-size:30px;color:var(--ink);white-space:nowrap}
.nav-link.active{color:#e0303a;text-decoration:underline;text-underline-offset:6px;text-decoration-thickness:2px}
.avatar{left:1068px;top:24px;width:52px;height:52px;border-radius:50%;background:var(--blue-soft)}
.hero-title{left:0;width:1200px;top:295px;text-align:center;font-family:var(--condensed);font-weight:400;font-size:84px;line-height:76px;color:var(--white)}
.hero-sub{left:0;width:1200px;top:464px;text-align:center;font-weight:600;font-size:26px;line-height:38px;color:var(--white)}
.btn-book{left:488px;top:570px;width:224px;height:52px;border-radius:10px;background:var(--teal);color:#111;font-weight:600;font-size:20px;white-space:nowrap;display:flex;align-items:center;justify-content:center}
.powered{left:488px;width:300px;top:632px;text-align:center;font-size:12px;font-weight:600;color:var(--white)}

/* features */
.feature{top:820px;width:320px;text-align:center}
.feature svg{display:block;margin:0 auto}
.feature-label{margin-top:22px;font-family:var(--condensed);font-size:32px;color:var(--ink)}

/* problem band */
.band{left:0;top:1050px;width:1200px;height:803px;background:var(--teal-pale)}
.card{left:163px;top:1169px;width:724px;height:605px;background:#f8fbfa;border-radius:6px}
.model{left:814px;top:1210px;width:271px;height:564px;background:linear-gradient(180deg,#c9a28a 0%,#6b4a3a 25%,#1d1d1f 45%,#2a2a2c 100%);border-radius:120px 120px 0 0}
.pain-1{left:192px;top:1252px;font-family:var(--condensed);font-weight:400;font-size:52px;line-height:56px;color:var(--magenta-mid);white-space:nowrap}
.pain-2{left:192px;top:1312px;width:620px;font-family:var(--condensed);font-weight:400;font-size:42px;line-height:44px;color:var(--magenta-mid)}
.pain-body{left:192px;top:1482px;width:540px;font-family:var(--condensed);font-size:26px;line-height:36px;color:#111}
.btn-talk{left:194px;top:1628px;width:184px;height:42px;border-radius:21px;background:var(--magenta-soft);font-family:var(--condensed);font-size:22px;color:#222;white-space:nowrap;display:flex;align-items:center;justify-content:center}

/* methods */
.methods-title{left:0;width:1200px;top:1898px;text-align:center;font-weight:600;font-size:42px;letter-spacing:4px}
.wheel{left:286px;top:1983px}
.method-label{font-family:'Nunito',sans-serif;font-size:15px;fill:var(--purple)}

/* blog */
.section-title{left:0;width:1200px;text-align:center;font-family:var(--condensed);font-weight:400;font-size:86px;color:var(--ink)}
.rule{height:2px;background:#222}
.video{left:81px;top:2949px;width:700px;height:467px;background:linear-gradient(135deg,#d97c3c,#c8622b);}
.video-bar{left:81px;top:3346px;width:700px;height:56px;background:#1f3554;display:flex;align-items:center;padding:0 26px;gap:14px;color:var(--white);font-family:var(--condensed);font-size:26px}
.track{flex:1;height:5px;background:var(--white)}
.post{background:#151a20}
.post-img{width:100%}
.post-body{padding:10px 14px;color:var(--white);position:relative}
.post-date{font-size:14px;font-weight:600}
.post-title{font-size:17px;color:var(--teal-mid);line-height:19px;letter-spacing:.5px}
.post-by{font-size:8px;text-align:right;margin-top:6px}
.bookmark{position:absolute;right:14px;top:10px}

/* coach */
.coach-name{left:225px;top:3922px;font-family:'Nunito',sans-serif;font-weight:800;font-size:38px;color:var(--teal);white-space:nowrap}
.btn-learn{left:401px;top:4007px;width:119px;height:33px;border-radius:17px;background:var(--teal);color:var(--white);font-size:10px;font-weight:600;display:flex;align-items:center;justify-content:center}
.coach-back{left:682px;top:3788px;width:447px;height:490px;background:var(--teal-wash)}
.coach-photo{left:643px;top:3748px;width:446px;height:491px;background:linear-gradient(160deg,#e8e6e2,#c9c3ba 55%,#9c958c);border-radius:90px 0 90px 0}
.play{left:597px;top:3965px;width:96px;height:96px;border-radius:50%;background:#fbf1dd;display:flex;align-items:center;justify-content:center}

/* schedule */
.schedule{left:0;top:4366px;width:1200px;height:486px;background:var(--teal-wash)}
.schedule-title{left:0;width:1200px;top:4410px;text-align:center;font-family:var(--condensed);font-weight:400;font-size:62px;color:#111}
.schedule-title span{color:var(--blue)}
.field{background:var(--white);border:1px solid #d8e4e2;font-family:var(--condensed);font-size:24px;color:var(--grey);padding:0 28px;display:flex;align-items:center;justify-content:space-between}
.caret{width:0;height:0;border-left:7px solid transparent;border-right:7px solid transparent;border-top:8px solid #555}

/* giveaway */
.giveaway{left:0;top:4852px;width:1200px;height:487px;background:linear-gradient(180deg,#8f8c86 0%,#b8a48c 35%,#9a7e62 65%,#5b4a3c 100%)}
.give-title{left:140px;width:630px;top:4998px;text-align:center;font-family:'Nunito',sans-serif;font-weight:700;font-size:37px;line-height:44px;color:var(--white)}
.give-body{left:100px;width:710px;top:5136px;text-align:center;font-family:'Nunito',sans-serif;font-weight:700;font-size:21px;line-height:42px;color:var(--white)}
.btn-download{left:359px;top:5234px;width:186px;height:42px;background:var(--magenta-mid);border-radius:4px;color:#222;font-family:'Nunito',sans-serif;font-weight:700;font-size:20px;white-space:nowrap;display:flex;align-items:center;justify-content:center}
.footer{left:0;top:5339px;width:1200px;height:33px;text-align:center;font-family:'Nunito',sans-serif;font-weight:700;font-size:17px;line-height:33px}
</style>
</head>
<body>

<!-- hero -->
<div class="abs hero" role="img" aria-label="Mountain lake at dusk with a wooden pier leading into calm water"></div>
<header class="abs nav">
  <div class="abs brand"><span class="brand-dot"></span><span>Kestrel Hollow</span></div>
  <a class="abs nav-link active" style="left:551px">Home</a>
  <a class="abs nav-link" style="left:672px">Blog</a>
  <a class="abs nav-link" style="left:776px">Coach</a>
  <a class="abs nav-link" style="left:885px">Contact us</a>
  <div class="abs avatar"></div>
</header>
<h1 class="abs hero-title">Say Good Bye To Diabetes,<br>Hypertension, Obesity &amp; PCOD</h1>
<p class="abs hero-sub">A 12 week lifestyle coaching programme to<br>reverse your disease condition®</p>
<div class="abs btn-book">Book Appointment</div>
<div class="abs powered">Powered by "Medibook"</div>

<!-- features -->
<div class="abs feature" style="left:136px">
  <svg width="110" height="110" viewBox="0 0 110 110" fill="none" stroke="#111" stroke-width="4" stroke-linejoin="round">
    <path d="M30 8h26M36 8v34L14 94h58L50 42V8"/><path d="M22 76h42"/><circle cx="40" cy="84" r="4"/>
    <path d="M78 40h20v60H78z"/><path d="M78 60h20"/>
  </svg>
  <div class="feature-label">Scientifically Validated</div>
</div>
<div class="abs feature" style="left:472px">
  <svg width="120" height="110" viewBox="0 0 120 110" fill="none" stroke="#111" stroke-width="4" stroke-linejoin="round" stroke-linecap="round">
    <circle cx="62" cy="52" r="26"/><path d="M62 36v32M70 42c-4-4-16-4-16 3s16 5 16 12-12 7-16 3"/>
    <path d="M6 78h18l20 12h40l26-18M6 100h28"/><path d="M90 10h20v24"/>
  </svg>
  <div class="feature-label">Simple &amp; Affordable</div>
</div>
<div class="abs feature" style="left:790px">
  <svg width="120" height="110" viewBox="0 0 120 110" fill="none" stroke="#111" stroke-width="4" stroke-linejoin="round" stroke-linecap="round">
    <path d="M60 6l5 10 11 1-8 8 2 11-10-5-10 5 2-11-8-8 11-1z"/>
    <circle cx="60" cy="52" r="10"/>
    <path d="M8 48l30 34h44l30-34M38 82l10 22h24l10-22"/>
  </svg>
  <div class="feature-label">Long-Term Results</div>
</div>

<!-- problem band -->
<div class="abs band"></div>
<div class="abs card"></div>
<div class="abs model" role="img" aria-label="Confident woman in a black dress, arms folded"></div>
<h2 class="abs pain-1">You shouldn't have to be on medication</h2>
<p class="abs pain-2">for the rest of your life. It's expensive and<br>can cause side effects...</p>
<p class="abs pain-body">You deserve a plan that will get you back to optimal health naturally and the support of professionals who care.</p>
<div class="abs btn-talk">TALK TO US NOW</div>

<!-- methods -->
<h2 class="abs methods-title">OUR METHODS</h2>
<svg class="abs wheel" width="620" height="620" viewBox="-310 -310 620 620">
  <g fill="#fff" stroke="#e2e1ea" stroke-width="4">
    <path id="seg" d="M10.5,-299.8 A300,300 0 0 1 204.6,-219.4 L99.6,-106.8 A146,146 0 0 0 5.1,-145.9 Z"/>
    <use href="#seg" transform="rotate(45)"/><use href="#seg" transform="rotate(90)"/><use href="#seg" transform="rotate(135)"/>
    <use href="#seg" transform="rotate(180)"/><use href="#seg" transform="rotate(225)"/><use href="#seg" transform="rotate(270)"/>
    <use href="#seg" transform="rotate(315)"/>
  </g>
  <g fill="#e3daeb">
    <path id="tip" d="M172,-240 L208,-218 L178,-200 Z"/>
    <use href="#tip" transform="rotate(45)"/><use href="#tip" transform="rotate(90)"/><use href="#tip" transform="rotate(135)"/>
    <use href="#tip" transform="rotate(180)"/><use href="#tip" transform="rotate(225)"/><use href="#tip" transform="rotate(270)"/>
    <use href="#tip" transform="rotate(315)"/>
  </g>
  <g fill="none" stroke="#6B429C" stroke-width="2.5" stroke-linecap="round" stroke-linejoin="round">
    <g transform="translate(-79,-250)"><circle cx="-8" cy="-10" r="4"/><circle cx="10" cy="-12" r="4"/><path d="M-14 10v-12h12v12M4 10v-14h12v14M-18 10h36"/></g>
    <g transform="translate(81,-245)"><path d="M-12 -6h24v20h-24z M-6 -6v-8h12v8 M-12 4h24"/></g>
    <g transform="translate(215,-112)"><path d="M-16 -2h32c0 10-6 16-16 16s-16-6-16-16z"/><circle cx="8" cy="-12" r="3"/><circle cx="15" cy="-18" r="2"/><path d="M-20 6h6"/></g>
    <g transform="translate(207,52)"><path d="M-18 -8v16M-12 -12v24M12 -12v24M18 -8v16M-12 0h24"/></g>
    <g transform="translate(92,176)"><circle cx="0" cy="6" r="10"/><path d="M-4 -4v-12h8v12M-6 -16h12"/></g>
    <g transform="translate(-86,166)"><circle cx="0" cy="-12" r="5"/><path d="M-22 10h44v8h-44z M-14 2h20l6 8M-18 18v6M18 18v6"/></g>
    <g transform="translate(-207,42)"><path d="M-16 2h26c0 8-6 12-13 12s-13-4-13-12zM10 4l12-4M-4 -4c-2-6 4-8 2-14M4 -4c-2-6 4-8 2-14"/></g>
    <g transform="translate(-209,-116)"><path d="M-14 -4c0-8 8-12 14-8 6-4 14 0 14 8 0 12-8 18-14 18s-14-6-14-18zM0 -12c0-4 2-8 6-10"/></g>
  </g>
  <g class="method-label" text-anchor="middle">
    <text x="-79" y="-210">Counselling/</text><text x="-79" y="-193">Stress</text><text x="-79" y="-176">Management</text>
    <text x="81" y="-206">Healthy</text><text x="81" y="-189">Grocery Shopping</text>
    <text x="215" y="-60">Hydrotherapy</text>
    <text x="207" y="101">Fitness Program</text>
    <text x="92" y="226">Health Education</text>
    <text x="-86" y="208">Therapeutic</text><text x="-86" y="225">Massage</text>
    <text x="-207" y="91">Cooking</text>
    <text x="-209" y="-74">Nutrition</text><text x="-209" y="-57">Empowerment</text>
  </g>
</svg>

<!-- blog -->
<div class="abs rule" style="left:413px;top:2853px;width:100px"></div>
<h2 class="abs section-title" style="top:2800px">Blog</h2>
<div class="abs rule" style="left:676px;top:2853px;width:100px"></div>
<div class="abs video" role="img" aria-label="Pill pack, glucose meter and insulin pen on an orange surface"></div>
<svg class="abs" style="left:420px;top:3142px" width="50" height="76" viewBox="0 0 50 76"><path d="M0 0L50 38L0 76Z" fill="#111"/></svg>
<div class="abs video-bar">
  <svg width="22" height="24" viewBox="0 0 22 24"><path d="M0 0L22 12L0 24Z" fill="#fff"/></svg>
  <span>00:00</span><div class="track"></div><span>01:32</span>
  <svg width="22" height="20" viewBox="0 0 22 20"><path d="M0 6h6l7-6v20l-7-6H0z" fill="#fff"/><path d="M16 5c3 3 3 7 0 10" stroke="#fff" stroke-width="2" fill="none"/></svg>
  <div style="width:40px;height:3px;background:#fff"></div>
</div>
<article class="abs post" style="left:812px;top:2926px;width:273px;height:257px">
  <div class="post-img" style="height:152px;background:linear-gradient(135deg,#f4a6c0,#e9b9a8)" role="img" aria-label="Close-up of a person's midsection against a pink background"></div>
  <div class="post-body">
    <svg class="bookmark" width="16" height="20" viewBox="0 0 16 20"><path d="M1 1h14v18l-7-5-7 5z" fill="none" stroke="#fff" stroke-width="2"/></svg>
    <div class="post-date">Feburary 14,2021</div>
    <div class="post-title">Is Diabetics Is Mother<br>of all diseases.</div>
    <div class="post-by">by Dr. Ada Moss</div>
  </div>
</article>
<article class="abs post" style="left:803px;top:3220px;width:270px;height:257px">
  <div class="post-img" style="height:155px;background:linear-gradient(180deg,#9fb4c8,#5d6470 60%,#2b2f36)" role="img" aria-label="Large hotel building facade"></div>
  <div class="post-body">
    <svg class="bookmark" width="16" height="20" viewBox="0 0 16 20"><path d="M1 1h14v18l-7-5-7 5z" fill="none" stroke="#fff" stroke-width="2"/></svg>
    <div class="post-date">Feburary 14,2021</div>
    <div class="post-title">Is Hoteling safe?</div>
    <div class="post-by">by Dr. Ada Moss</div>
  </div>
</article>

<!-- coach -->
<div class="abs rule" style="left:326px;top:3688px;width:137px"></div>
<h2 class="abs section-title" style="top:3648px;font-size:68px">OUR<span style="color:var(--teal-light)">Coach</span></h2>
<div class="abs rule" style="left:710px;top:3688px;width:135px"></div>
<div class="abs coach-name">Dr. Lena Hart</div>
<div class="abs btn-learn">Learn more</div>
<div class="abs coach-back"></div>
<div class="abs coach-photo" role="img" aria-label="Smiling coach in glasses holding a clipboard in a bright office"></div>
<div class="abs play"><svg width="34" height="34" viewBox="0 0 34 34"><path d="M4 2L32 17L4 32Z" fill="#f4a623"/></svg></div>

<!-- schedule -->
<section class="abs schedule"></section>
<h2 class="abs schedule-title">SCHEDULE THE <span>MEETING</span></h2>
<div class="abs field" style="left:142px;top:4514px;width:444px;height:57px">Name</div>
<div class="abs field" style="left:605px;top:4514px;width:445px;height:57px">Email</div>
<div class="abs field" style="left:142px;top:4623px;width:288px;height:58px">Date</div>
<div class="abs field" style="left:451px;top:4623px;width:288px;height:58px">Time</div>
<div class="abs field" style="left:760px;top:4623px;width:290px;height:58px">Gander<span class="caret"></span></div>
<div class="abs field" style="left:142px;top:4733px;width:444px;height:59px;font-family:'Montserrat',sans-serif;font-size:18px;color:#555">Country<span class="caret" style="border-top-width:6px;border-left-width:5px;border-right-width:5px"></span></div>

<!-- giveaway -->
<section class="abs giveaway" role="img" aria-label="Older couple sitting together on a lakeside pier at sunset"></section>
<h2 class="abs give-title">Give Away – Understanding<br>Diabetes</h2>
<p class="abs give-body">Download your free copy of tips to reverse the effects of<br>Diabetes naturally and at home.</p>
<div class="abs btn-download">DOWNLOAD NOW</div>

<footer class="abs footer">COPY RIGHT 2022</footer>
</body>
</html>
```